Top International Talent Management Needs creative business card design

We manage actors careers and book them liaising and promoting their profiles internationally through Casting Directors, Producers, Directors, Publicists etc. We need clearly visable contact details but with a design that reflects our status and creativity of TV, Feature Film industry. Our logo is attached and needs to relate and our website is www.marrowlanepeople.com
No flame designs please but please incorporate logo colours.

Target Market(s)

Clients

Industry/Entity Type

Film Production

Contact Information for Business Card

Director Rosalind Tebbett
Suite F, Building 4, Harrowgate Sound Stages, Tullick Vale, Port Carrow, KV 4870

Font styles to use
Sans Serif

Colors
ec1f27

Requirements
Nice to have
• Colours should relate to logo attached and type can relate again to type in the logo design.
Should not have
• No Flames designs and best to be not too obvious with the film designs eiither. Needs to be more creative and modern

```html
<!DOCTYPE html>
<html lang="en">
<head>
<meta charset="utf-8">
<title>Marrow Lane People – Business Card</title>
<link rel="stylesheet" href="https://fonts.googleapis.com/css2?family=Exo+2:wght@400;500;600&display=swap">
<style>
  :root {
    --brand-red: #ec1f27;
    --band-red: #d01a2a;
    --ink: #1c1c1c;
    --rule: #4a4a4a;
    --card: #ffffff;
    --backdrop: #e9e7e4;
  }
  * { box-sizing: border-box; margin: 0; padding: 0; }
  html, body { width: 1200px; height: 885px; overflow: hidden; }
  body {
    background: var(--backdrop);
    font-family: "Exo 2", sans-serif;
    position: relative;
  }
  .card {
    position: absolute;
    left: 280px;
    width: 640px;
    height: 366px;
    background: linear-gradient(135deg, #ffffff 0%, #f3f3f3 100%);
    box-shadow: 0 6px 18px rgba(0,0,0,0.18);
    overflow: hidden;
  }
  .card-front { top: 34px; }
  .card-back { top: 466px; }

  /* front */
  .front-brand {
    position: absolute;
    left: 40px;
    top: 120px;
    width: 230px;
    display: flex;
    align-items: center;
    gap: 10px;
  }
  .brand-mark {
    width: 16px; height: 16px;
    background: var(--brand-red);
    flex: none;
  }
  .brand-name {
    color: var(--brand-red);
    font-weight: 600;
    font-size: 27px;
    line-height: 1.05;
    letter-spacing: 0.5px;
  }
  .divider {
    position: absolute;
    left: 290px;
    top: 40px;
    width: 1px;
    height: 220px;
    background: var(--rule);
  }
  .contact-block {
    position: absolute;
    left: 318px;
    top: 46px;
    right: 20px;
  }
  .person-name {
    color: var(--brand-red);
    font-weight: 600;
    font-size: 26px;
  }
  .person-title {
    color: var(--ink);
    font-size: 20px;
    margin-top: 2px;
    margin-bottom: 26px;
  }
  .contact-row {
    display: flex;
    align-items: center;
    gap: 10px;
    color: var(--ink);
    font-size: 15px;
    margin-bottom: 9px;
  }
  .contact-icon {
    width: 19px; height: 19px;
    background: var(--brand-red);
    flex: none;
    display: block;
  }
  .address-band {
    position: absolute;
    left: 0; right: 0; bottom: 0;
    height: 44px;
    background: linear-gradient(180deg, var(--brand-red), var(--band-red));
    color: #fff;
    font-size: 15.5px;
    letter-spacing: 0.2px;
    white-space: nowrap;
    display: flex;
    align-items: center;
    justify-content: center;
  }

  /* back */
  .back-brand {
    position: absolute;
    inset: 0;
    display: flex;
    align-items: center;
    justify-content: center;
    gap: 16px;
  }
  .back-brand .brand-mark { width: 26px; height: 26px; }
  .back-brand .brand-name { font-size: 52px; }
</style>
</head>
<body>
  <section class="card card-front" aria-label="Business card front">
    <div class="front-brand">
      <span class="brand-mark"></span>
      <span class="brand-name">Marrow Lane People</span>
    </div>
    <div class="divider"></div>
    <div class="contact-block">
      <div class="person-name">Rosalind Tebbett</div>
      <div class="person-title">Director</div>
      <div class="contact-row">
        <svg class="contact-icon" viewBox="0 0 20 20" aria-hidden="true">
          <path d="M6 4h3l1 4-2 1c1 2 2 3 4 4l1-2 4 1v3c0 1-1 1-2 1C9 16 4 11 4 6c0-1 1-2 2-2z" fill="#fff"/>
        </svg>
        <span>+61 (0) 400 555 019</span>
      </div>
      <div class="contact-row">
        <svg class="contact-icon" viewBox="0 0 20 20" aria-hidden="true">
          <rect x="4" y="6" width="12" height="8" fill="none" stroke="#fff" stroke-width="1.4"/>
          <path d="M4 6l6 5 6-5" fill="none" stroke="#fff" stroke-width="1.4"/>
        </svg>
        <span>rosalind@marrowlanepeople.com</span>
      </div>
      <div class="contact-row">
        <svg class="contact-icon" viewBox="0 0 20 20" aria-hidden="true">
          <circle cx="10" cy="10" r="6" fill="none" stroke="#fff" stroke-width="1.3"/>
          <ellipse cx="10" cy="10" rx="2.6" ry="6" fill="none" stroke="#fff" stroke-width="1.1"/>
          <path d="M4 10h12" stroke="#fff" stroke-width="1.1"/>
        </svg>
        <span>www.marrowlanepeople.com</span>
      </div>
    </div>
    <div class="address-band">Suite F, Building 4, Harrowgate Sound Stages, Tullick Vale, Port Carrow, KV 4870</div>
  </section>

  <section class="card card-back" aria-label="Business card back">
    <div class="back-brand">
      <span class="brand-mark"></span>
      <span class="brand-name">Marrow Lane People</span>
    </div>
  </section>
</body>
</html>
```